Creative Brief
Eastmoor Directorate - Bahrain
Business Cards + Stationary materials.
Simple
Tariq Yousef Al-Mansoori
Head of Financial Affairs
P.O. Box 37182, Westbrook. Eastmoor Region
talmansoori@eastmoor-dir.example
www.eastmoor-dir.example
We would like the design to include the following colors : cyan, golden & silver. But we are open to new ideas that match our new logo.
Stationary items include :
- A4 letterhead ( would prefer the logo in the top middle section so that we can write the office name on either side of the A4 paper. We would like to use the attached watermark image ( you can change the color to match the theme )
- Notepad
- Presentation folder
- Envelopes ( A4, A3, basically the whole nine yards)
a short explanation on the attached files :
* ED Logo : main logo that represents our office (available in B&W and colored)
* Watermark : design we want as a watermark on the stationary
* Horizon : logo (available in different sizes) that should appear close to the address line and should appear on all stationary materials and business cards. This represents Bahrain horizon plan for economic development, more info can be found here : http://www.horizonplan.example/web/ , or http://wiki.example.org/wiki/Bahrain_Horizon_Plan
We would like to also point out that the back side of the business card MUST include the same information as the front but in Arabic language, you can find the translated info below.
Name : طارق يوسف المنصوري
Title : رئيس الموارد المالية
address :
ص.ب 37182، ويستبروك. منطقة إيستمور
all the other info should be the same.
We wouldn't mind seeing different types of fonts as long as they are professional, serious and formal.
ED Logo : main logo that represents our office - in black and white
ED Logo : main logo that represents our office - colored
design we want as a watermark on the stationary
logo that should appear close to the address line and should appear on all stationary materials and business cards. This represents Bahrain horizon plan for economic development, more info can be found here : http://www.horizonplan.example/web/ ,or http://wiki.example.org/wiki/Bahrain_Horizon_Plan

```html
<!DOCTYPE html>
<html lang="en">
<head>
<meta charset="utf-8">
<title>Eastmoor Directorate – Stationery</title>
<link href="https://fonts.googleapis.com/css2?family=Open+Sans:wght@400;600;700&family=Noto+Naskh+Arabic:wght@400;700&family=Dancing+Script:wght@500&display=swap" rel="stylesheet">
<style>
:root{
  --navy:#1d4b9a;
  --navy-deep:#143a7d;
  --navy-light:#2f63b8;
  --gold:#c9a65a;
  --paper:#ffffff;
  --ink:#3a3a3a;
  --muted:#7b7b7b;
  --accent:#c8202f;
  --ground:#e4e6ea;
  --watermark:#eceef1;
}
*{box-sizing:border-box;margin:0;padding:0}
html,body{width:1200px;height:847px;overflow:hidden}
body{background:var(--ground);font-family:"Open Sans",Arial,sans-serif;color:var(--ink);position:relative}
.piece{position:absolute;background:var(--paper);box-shadow:0 3px 10px rgba(0,0,0,.18);overflow:hidden}
.band{position:absolute;left:0;right:0;top:0;background:linear-gradient(135deg,var(--navy-light),var(--navy) 50%,var(--navy-deep));border-bottom:3px solid var(--gold)}
.badge{position:absolute;left:50%;transform:translateX(-50%);background:var(--paper);border-radius:50%;border:2px solid var(--gold);display:flex;align-items:center;justify-content:center;text-align:center;font-weight:700;color:var(--navy);line-height:1.15}
.horizon{font-weight:700;color:var(--accent)}
.watermark{position:absolute;background:linear-gradient(90deg,rgba(236,238,241,0),var(--watermark) 30%,var(--watermark) 70%,rgba(236,238,241,0));border-radius:40px}

/* letterhead */
.letterhead{left:50px;top:56px;width:520px;height:735px}
.letterhead .band{height:108px}
.letterhead .badge{top:62px;width:170px;height:86px;font-size:13px}
.letter-body{position:absolute;left:46px;right:46px;top:180px;font-size:9.5px;line-height:1.65;z-index:1}
.letter-body p{margin-bottom:12px}
.letter-body ul{margin:0 0 12px 18px}
.signature{font-family:"Dancing Script",cursive;font-size:22px;color:var(--navy-deep);margin-top:6px}
.letterhead .watermark{left:150px;top:530px;width:300px;height:110px}
.letter-foot{position:absolute;left:0;right:0;bottom:0;height:58px;border-top:3px solid var(--gold);display:flex;align-items:center;justify-content:space-between;padding:0 40px;font-size:8.5px;color:var(--muted)}
.letter-foot .horizon{font-size:16px}

/* envelope */
.envelope{left:620px;top:56px;width:530px;height:265px}
.envelope .band{height:70px}
.envelope .badge{top:34px;width:130px;height:66px;font-size:10.5px;left:110px}
.envelope .watermark{right:40px;top:120px;width:260px;height:100px}
.envelope-foot{position:absolute;left:28px;bottom:20px;font-size:8px;color:var(--muted);line-height:1.5}
.envelope .horizon{position:absolute;right:32px;bottom:20px;font-size:15px}

/* business cards */
.card{top:350px;width:255px;height:160px}
.card-front{left:620px}
.card-back{left:895px}
.card .band{height:52px}
.card .badge{top:22px;width:100px;height:52px;font-size:8.5px}
.card-info{position:absolute;left:16px;right:16px;top:86px;font-size:7.5px;line-height:1.5;color:var(--ink)}
.card-name{font-size:10.5px;font-weight:700;color:var(--navy)}
.card-title{font-size:8px;color:var(--muted);margin-bottom:4px}
.card-back .card-info{font-family:"Noto Naskh Arabic",serif;direction:rtl;text-align:right}
.card-back .card-name{font-size:11.5px}
.card .horizon{position:absolute;font-size:10px;bottom:10px}
.card-front .card-info{right:70px}
.card-back .card-info{left:70px}
.card-front .horizon{right:14px}
.card-back .horizon{left:14px}

/* compliment slip */
.slip{left:620px;top:540px;width:530px;height:251px}
.slip .band{height:66px}
.slip .badge{top:30px;width:126px;height:64px;font-size:10.5px}
.slip .watermark{left:135px;top:130px;width:260px;height:70px}
.slip-title{position:absolute;left:0;right:0;top:106px;text-align:center;font-size:11px;letter-spacing:2px;color:var(--navy);font-weight:600;z-index:1}
.slip-foot{position:absolute;left:0;right:0;bottom:0;height:40px;border-top:3px solid var(--gold);display:flex;align-items:center;justify-content:space-between;padding:0 28px;font-size:8px;color:var(--muted)}
.slip-foot .horizon{font-size:14px}
</style>
</head>
<body>

<section class="piece letterhead">
  <div class="band" role="img" aria-label="Blue band with geometric pattern"></div>
  <div class="badge">Eastmoor<br>Directorate</div>
  <div class="watermark" role="img" aria-label="Faint Arabic calligraphy watermark"></div>
  <div class="letter-body">
    <p>Dear Mr. First Last</p>
    <p>We are pleased to confirm receipt of your recent request and thank you for your continued cooperation with our office. Our team has reviewed the details provided and will prepare the required documents within the agreed period. Please find below a summary of the main points discussed during our last meeting.</p>
    <ul>
      <li>Review of annual budget</li>
      <li>Update of service records</li>
      <li>Schedule of next meeting</li>
    </ul>
    <p>Should you require any further information, please do not hesitate to contact the office directly. We look forward to working with you on the next stage of this project and to continued success together.</p>
    <p>Sincerely,</p>
    <div class="signature">Daniel Hart</div>
    <p>Daniel Hart</p>
  </div>
  <footer class="letter-foot">
    <span>P.O. Box 37182, Westbrook. Eastmoor Region<br>www.eastmoor-dir.example</span>
    <span class="horizon">Horizon</span>
  </footer>
</section>

<section class="piece envelope">
  <div class="band" role="img" aria-label="Blue band with geometric pattern"></div>
  <div class="badge">Eastmoor<br>Directorate</div>
  <div class="watermark" role="img" aria-label="Faint Arabic calligraphy watermark"></div>
  <div class="envelope-foot">P.O. Box 37182, Westbrook. Eastmoor Region<br>www.eastmoor-dir.example</div>
  <span class="horizon">Horizon</span>
</section>

<section class="piece card card-front">
  <div class="band" role="img" aria-label="Blue band with geometric pattern"></div>
  <div class="badge">Eastmoor<br>Directorate</div>
  <div class="card-info">
    <div class="card-name">Tariq Yousef Al-Mansoori</div>
    <div class="card-title">Head of Financial Affairs</div>
    T +00 555 0148 &nbsp; F +00 555 0149<br>
    talmansoori@eastmoor-dir.example<br>
    P.O. Box 37182, Westbrook. Eastmoor Region
  </div>
  <span class="horizon">Horizon</span>
</section>

<section class="piece card card-back" lang="ar">
  <div class="band" role="img" aria-label="Blue band with geometric pattern"></div>
  <div class="badge">Eastmoor<br>Directorate</div>
  <div class="card-info">
    <div class="card-name">طارق يوسف المنصوري</div>
    <div class="card-title">رئيس الموارد المالية</div>
    <span dir="ltr">+00 555 0148</span><br>
    talmansoori@eastmoor-dir.example<br>
    ص.ب 37182، ويستبروك. منطقة إيستمور
  </div>
  <span class="horizon">Horizon</span>
</section>

<section class="piece slip">
  <div class="band" role="img" aria-label="Blue band with geometric pattern"></div>
  <div class="badge">Eastmoor<br>Directorate</div>
  <div class="watermark" role="img" aria-label="Faint Arabic calligraphy watermark"></div>
  <div class="slip-title">EASTMOOR DIRECTORATE</div>
  <footer class="slip-foot">
    <span>P.O. Box 37182, Westbrook. Eastmoor Region &nbsp;·&nbsp; www.eastmoor-dir.example</span>
    <span class="horizon">Horizon</span>
  </footer>
</section>

</body>
</html>
```